Business Card Design

I need a business card for my rental business. The business is named:
Hire a Vorlatrike Brenmoor
www.hireavorlatrikebrenmoor.example
(555) 014-2937
This will be a business card that I will leave at other businesses as advertisement so it needs to have the name, website, and phone number.
Please feel free to be creative. This is a new business so I have no designs.
Thank you very much for your time and I look forward to receiving your designs
Target Market(s)
Local rental customers
Industry/Entity Type
Business
Contact Information for Business Card
Please check out my website:
Other font styles liked:
- anything creative
Colors
Designer to choose colors to be used in the design.
Requirements
Must have
- Business name, phone, website. Rentals available hourly or daily. Book online

```html
<!DOCTYPE html>
<html lang="en">
<head>
<meta charset="utf-8">
<title>Hire a Vorlatrike Brenmoor – Business Card</title>
<link href="https://fonts.googleapis.com/css2?family=Roboto+Condensed:wght@400;700&display=swap" rel="stylesheet">
<style>
  :root {
    --backdrop: #d9dadc;
    --card-dark: #58595b;
    --card-light: #f4f4f2;
    --ink-dark: #3a3b3d;
    --ink-light: #ffffff;
    --shadow: rgba(0, 0, 0, 0.22);
  }
  * { box-sizing: border-box; margin: 0; padding: 0; }
  html, body {
    width: 1200px;
    height: 877px;
    overflow: hidden;
    background: var(--backdrop);
    font-family: "Roboto Condensed", "Arial Narrow", sans-serif;
  }
  .canvas {
    width: 1200px;
    height: 877px;
    display: flex;
    align-items: center;
    justify-content: center;
    gap: 60px;
  }
  .card {
    width: 510px;
    height: 292px;
    flex-shrink: 0;
    border-radius: 4px;
    box-shadow: 0 10px 24px var(--shadow);
    position: relative;
    overflow: hidden;
  }
  .brand-dot {
    display: block;
    flex-shrink: 0;
    border-radius: 50%;
  }
  .brand-name {
    font-weight: 700;
    text-transform: uppercase;
    white-space: nowrap;
    line-height: 1.1;
  }

  /* Front */
  .card-front {
    background: var(--card-dark);
    color: var(--ink-light);
    display: flex;
    flex-direction: column;
    align-items: center;
    justify-content: center;
    gap: 22px;
    padding: 0 30px;
  }
  .card-front .brand-dot {
    width: 86px;
    height: 86px;
    border: 6px solid var(--ink-light);
  }
  .card-front .brand-name {
    font-size: 32px;
    letter-spacing: 1px;
  }

  /* Back */
  .card-back {
    background: var(--card-light);
    color: var(--ink-dark);
  }
  .details {
    position: absolute;
    left: 0;
    right: 0;
    top: 0;
    bottom: 62px;
    display: flex;
    flex-direction: column;
    align-items: center;
    justify-content: center;
    text-align: center;
    padding: 0 20px;
  }
  .card-back .brand {
    display: flex;
    align-items: center;
    gap: 10px;
    margin-bottom: 14px;
  }
  .card-back .brand-dot {
    width: 26px;
    height: 26px;
    border: 3px solid var(--ink-dark);
  }
  .card-back .brand-name {
    font-size: 22px;
    letter-spacing: 0.5px;
  }
  .contact-line {
    font-size: 17px;
    line-height: 1.45;
  }
  .service-band {
    position: absolute;
    left: 0;
    right: 0;
    bottom: 0;
    height: 62px;
    background: var(--card-dark);
    color: var(--ink-light);
    display: flex;
    flex-direction: column;
    align-items: center;
    justify-content: center;
    text-align: center;
    font-size: 15px;
    line-height: 1.35;
  }
</style>
</head>
<body>
  <main class="canvas">
    <section class="card card-front" aria-label="Card front">
      <span class="brand-dot" aria-hidden="true"></span>
      <h1 class="brand-name">Hire a Vorlatrike Brenmoor</h1>
    </section>

    <section class="card card-back" aria-label="Card back">
      <div class="details">
        <div class="brand">
          <span class="brand-dot" aria-hidden="true"></span>
          <h2 class="brand-name">Hire a Vorlatrike Brenmoor</h2>
        </div>
        <p class="contact-line phone">(555) 014-2937</p>
        <p class="contact-line website">www.hireavorlatrikebrenmoor.example</p>
        <p class="contact-line address">RM-812, Brenmoor, Texas 70019, United States</p>
      </div>
      <div class="service-band">
        <p class="service-note">Rentals available hourly or daily</p>
        <p class="service-cta">Book Online</p>
      </div>
    </section>
  </main>
</body>
</html>
```